Pain Seminar Flyer 8.5x11

We are having a FREE seminar on Pain for our Bootcamp members at our gym. We are looking for a great looking flyer with pictures and a design to draw people in. I have attached our logo, pictures of the 2 speakers and a Word document of the flyer information needed. PLEASE PLEASE make our head shots small and in a circle like the example flyer we attached but obviously make the flyer much much nicer than the example. Also we attached pic ideas about pain.
- This must be in PSD. format WITH LAYERS and fonts so we can edit the time or reuse the flyer.
- Size 8.5x11
- Attached info. with pics and logo (along with other pics of pain!)
Thank you!
Gym

```html
<!DOCTYPE html>
<html lang="en">
<head>
<meta charset="utf-8">
<title>Free Pain Seminar Flyer</title>
<link rel="stylesheet" href="https://fonts.googleapis.com/css2?family=Oswald:wght@300;400;500;700&family=Playfair+Display:wght@900&family=Montserrat:wght@400;500&display=swap">
<style>
  :root {
    --page: #e6e6e9;
    --ink-dark: #141414;
    --ink-mid: #2b2b2b;
    --blue: #3f86d0;
    --blue-bright: #2f7fd3;
    --orange: #c97b2f;
    --orange-icon: #c06a1c;
    --white: #ffffff;
    --grey-box: #4a4a4a;
    --frame: #8a8a8a;
  }
  * { margin: 0; padding: 0; box-sizing: border-box; }
  html, body { width: 1041px; height: 1200px; overflow: hidden; background: var(--page); }
  .flyer {
    position: absolute; left: 70px; top: 18px; width: 900px; height: 1163px; overflow: hidden;
    background: radial-gradient(ellipse at 50% 30%, #3a3a3a 0%, #222 45%, var(--ink-dark) 100%);
    font-family: "Oswald", sans-serif; color: var(--white);
  }
  .edge { position: absolute; left: 0; width: 900px; }
  .edge--top { top: 0; height: 110px; }
  .edge--bottom { bottom: 0; height: 60px; }
  .abs { position: absolute; }

  .pain-icon { width: 56px; height: 56px; border-radius: 50%; transform: translateX(-50%); top: 102px; }
  .pain-icon--back { left: 246px; background: var(--blue); }
  .pain-icon--shoulder { left: 448px; background: var(--orange-icon); }
  .pain-icon--knee { left: 650px; background: var(--white); }
  .pain-tag { top: 171px; height: 34px; font-size: 25px; font-weight: 400; line-height: 34px; text-align: center; }
  .pain-tag--back { left: 171px; width: 145px; background: var(--blue-bright); }
  .pain-tag--shoulder { left: 347px; width: 203px; background: var(--orange-icon); }
  .pain-tag--knee { left: 575px; width: 147px; background: var(--white); color: #111; }

  .headline {
    top: 232px; left: 0; width: 900px; text-align: center;
    font-family: "Playfair Display", serif; font-weight: 900; font-size: 118px; line-height: 118px;
    transform: scaleX(0.78); letter-spacing: -1px;
  }
  .subhead { top: 350px; left: 0; width: 900px; text-align: center; font-size: 70px; line-height: 80px; font-weight: 400; color: var(--blue-bright); }

  .cta-band { top: 449px; left: 0; width: 900px; height: 194px; background: var(--orange); }
  .cta-line { left: 0; width: 900px; text-align: center; font-size: 38px; line-height: 44px; font-weight: 400; }
  .cta-line--one { top: 467px; }
  .cta-line--two { top: 516px; }
  .cta-chip { display: inline-block; padding: 0 6px; border-radius: 5px; font-weight: 500; }
  .cta-chip--dark { background: var(--grey-box); }
  .cta-chip--blue { background: var(--blue-bright); font-size: 44px; }
  .phone { top: 570px; left: 0; width: 900px; text-align: center; font-size: 60px; line-height: 66px; font-weight: 700; }
  .phone svg { width: 40px; height: 40px; vertical-align: middle; margin-right: 22px; position: relative; top: -6px; }

  .agenda-frame { top: 673px; left: 63px; width: 805px; height: 201px; border: 1px solid var(--frame); }
  .agenda { top: 692px; left: 90px; list-style: none; }
  .agenda li { font-size: 26px; font-weight: 300; line-height: 41.5px; padding-left: 34px; position: relative; }
  .agenda li::before {
    content: ""; position: absolute; left: 0; top: 14px; width: 15px; height: 15px;
    border: 3px solid var(--blue-bright); border-radius: 50%;
  }
  .calendar { top: 698px; left: 674px; width: 52px; height: 52px; border: 2px solid var(--blue-bright); border-radius: 50%; }
  .calendar svg { width: 48px; height: 48px; }
  .event-date { top: 770px; left: 550px; width: 300px; text-align: center; font-size: 25px; line-height: 34px; font-weight: 400; }
  .event-time { top: 805px; left: 550px; width: 300px; text-align: center; font-size: 50px; line-height: 58px; font-weight: 500; }

  .brand { top: 924px; left: 67px; width: 310px; font-size: 36px; line-height: 40px; font-weight: 700; letter-spacing: 1px; }
  .contact { left: 67px; font-size: 22px; line-height: 28px; font-weight: 400; display: flex; align-items: center; gap: 10px; }
  .contact svg { width: 24px; height: 24px; }
  .contact--address { top: 1032px; }
  .contact--web { top: 1074px; }

  .speaker { top: 907px; width: 170px; text-align: center; }
  .speaker--one { left: 493px; }
  .speaker--two { left: 691px; }
  .speaker__photo {
    width: 135px; height: 135px; margin: 0 auto; border-radius: 50%; border: 4px solid var(--white);
    box-shadow: 0 0 0 3px #111;
  }
  .speaker--one .speaker__photo { background: radial-gradient(circle at 50% 45%, #c9a483 0%, #7a6a48 55%, #3f4a2c 100%); }
  .speaker--two .speaker__photo { background: radial-gradient(circle at 50% 45%, #d2926c 0%, #a5a8ad 60%, #6f7378 100%); }
  .speaker__name { font-family: "Montserrat", sans-serif; font-size: 19px; line-height: 24px; margin-top: 14px; font-weight: 500; }
  .speaker__creds { font-family: "Montserrat", sans-serif; font-size: 13px; line-height: 18px; }
  .divider { top: 907px; left: 678px; width: 2px; height: 198px; background: #ddd; }
</style>
</head>
<body>
<main class="flyer">
  <svg class="edge edge--top" viewBox="0 0 900 110" preserveAspectRatio="none" aria-hidden="true">
    <path fill="#3f86d0" d="M0 0H900V18L880 22 870 40 850 28 830 42 800 30 770 38 740 26 720 40 690 30 660 44 630 34 600 48 570 40 540 52 510 44 480 58 450 50 420 60 390 54 360 64 330 58 300 66 270 60 240 70 210 62 180 72 150 64 120 74 90 66 60 76 30 68 0 78Z"/>
    <path fill="#4a4a4a" d="M640 50 680 34 720 44 760 28 800 36 840 24 880 30 900 20V100L860 90 820 96 780 84 740 90 700 80 660 72Z"/>
  </svg>

  <div class="abs pain-icon pain-icon--back" role="img" aria-label="Pictogram of a person with back pain"></div>
  <div class="abs pain-icon pain-icon--shoulder" role="img" aria-label="Pictogram of a person with shoulder pain"></div>
  <div class="abs pain-icon pain-icon--knee" role="img" aria-label="Pictogram of a person with knee pain"></div>
  <div class="abs pain-tag pain-tag--back">BACK PAIN?</div>
  <div class="abs pain-tag pain-tag--shoulder">SHOULDER PAIN?</div>
  <div class="abs pain-tag pain-tag--knee">KNEE PAIN?</div>

  <h1 class="abs headline">FREE SEMINAR</h1>
  <h2 class="abs subhead">ON HOW TO STOP PAIN</h2>

  <div class="abs cta-band"></div>
  <p class="abs cta-line cta-line--one">LIMITED SPACE SO DON'T WAIT TO <span class="cta-chip cta-chip--dark">SIGN UP</span></p>
  <p class="abs cta-line cta-line--two">RESERVATIONS REQUIRED. <span class="cta-chip cta-chip--blue">CALL US TODAY</span></p>
  <p class="abs phone"><svg viewBox="0 0 40 40" aria-hidden="true"><circle cx="20" cy="20" r="17" fill="none" stroke="#fff" stroke-width="2.5"/><path fill="#fff" d="M13 11c1-1 2-1 3 0l2 3c.6 1 .3 2-.5 2.6l-1 .8c1 2.3 2.8 4.1 5 5l.8-1c.6-.8 1.6-1.1 2.6-.5l3 2c1 .7 1 1.9 0 3l-1.5 1.5c-1.5 1.5-5 .5-8.5-3s-4.5-7-3-8.5Z"/></svg>555-014-2290</p>

  <div class="abs agenda-frame"></div>
  <ul class="abs agenda">
    <li>How to Get Out of Pain</li>
    <li>What to do When an Exercise Hurts</li>
    <li>How Exercise Helps Pain</li>
    <li>Q &amp; A to Find Extraordinary Health</li>
  </ul>
  <div class="abs calendar"><svg viewBox="0 0 48 48" aria-hidden="true"><g fill="none" stroke="#2f7fd3" stroke-width="2.2"><rect x="13" y="15" width="20" height="18" rx="2"/><path d="M13 20H33M18 12V17M28 12V17"/><circle cx="32" cy="32" r="6" fill="#1c1c1c"/><path d="M32 29V32H34.5"/></g></svg></div>
  <p class="abs event-date">THURSDAY, APRIL 13th</p>
  <p class="abs event-time">7:30PM-9PM</p>

  <p class="abs brand">COREVIA FIT<br>BOOTCAMPS</p>
  <p class="abs contact contact--address"><svg viewBox="0 0 24 24" aria-hidden="true"><circle cx="12" cy="12" r="11" fill="none" stroke="#fff" stroke-width="1.5"/><path fill="#fff" d="M12 5a4.5 4.5 0 0 0-4.5 4.5C7.5 13 12 19 12 19s4.5-6 4.5-9.5A4.5 4.5 0 0 0 12 5Zm0 6.3a1.8 1.8 0 1 1 0-3.6 1.8 1.8 0 0 1 0 3.6Z"/></svg>18 Elm Row, Ashford, CO 80000</p>
  <p class="abs contact contact--web"><svg viewBox="0 0 24 24" aria-hidden="true"><circle cx="12" cy="12" r="11" fill="none" stroke="#fff" stroke-width="1.5"/><g fill="none" stroke="#fff" stroke-width="1.2"><circle cx="12" cy="12" r="6"/><ellipse cx="12" cy="12" rx="2.6" ry="6"/><path d="M6 12H18"/></g></svg>www.coreviafit.com</p>

  <div class="abs speaker speaker--one">
    <div class="speaker__photo" role="img" aria-label="Head shot of speaker Daniel Hart"></div>
    <p class="speaker__name">Daniel Hart,</p>
    <p class="speaker__creds">PT, DPT, OCS</p>
  </div>
  <div class="abs divider"></div>
  <div class="abs speaker speaker--two">
    <div class="speaker__photo" role="img" aria-label="Head shot of speaker Marcus Lane"></div>
    <p class="speaker__name">Marcus Lane</p>
    <p class="speaker__creds">MS, CSCS, FMS</p>
  </div>

  <svg class="edge edge--bottom" viewBox="0 0 900 60" preserveAspectRatio="none" aria-hidden="true">
    <path fill="#3f86d0" d="M0 60H900V6L870 18 840 8 810 20 780 10 750 22 720 12 690 24 660 14 630 26 600 16 570 28 540 18 510 30 480 20 450 30 420 20 390 30 360 18 330 28 300 16 270 26 240 14 210 24 180 12 150 22 120 10 90 20 60 8 30 18 0 10Z"/>
  </svg>
</main>
</body>
</html>
```